Media Services Start-up -- Corporate Website and Logo Design. Inspiration required!

We need a logo design and corporate website design, including coding, for our start-up business.
Brenvora’s value proposition is based on bringing together media content from a vast number of geographies globally, adding human and AI curation, translation and editing, and delivering the content using tailored customer interfaces. On the one hand, the business brings together media coverage from all over the world, and on the other it brings together content, human skills and technology to deliver a supreme customer experience.
Brenvora is a B2B media monitoring and analytics business with emphasis on global customers. Brenvora's service offering is centred around sourcing media content from different markets, processing, storing and delivering the content and insights derived from it using an online platform / mobile app.
The messaging we want to create through the logo is:
- Global scope
- Speed of delivery
- Cost-efficiency
- Multi-lingual
- Tailor-made
- Trustworthy
Target Market(s)
Business to business, PR / Communications, Media, Marketing
Logo Text
Brenvora
Coding
Coded - Design and coding required
Number of Pages Required
5+ page
Font styles to use
Other font styles liked:
- See Design Brief for details
Colors
Designer to choose colors to be used in the design.

```html
<!DOCTYPE html>
<html lang="en">
<head>
<meta charset="utf-8">
<title>Brenvora — Global Media Intelligence</title>
<link rel="stylesheet" href="https://fonts.googleapis.com/css2?family=Roboto:wght@400;500;700&display=swap">
<style>
:root{
  --board:#a9a9a9;
  --black:#000;
  --white:#fff;
  --teal:#3fab95;
  --ink:#1a1a1a;
  --body:#333;
  --muted:#8a8a8a;
  --band:#ecebec;
  --shadow:#cfcfcf;
  --panel:rgba(38,40,42,.93);
}
*{box-sizing:border-box;margin:0;padding:0}
html,body{width:1200px;height:2682px;overflow:hidden}
body{background:var(--board);font-family:'Roboto',sans-serif;position:relative;color:var(--body)}
.page{position:absolute;left:71px;width:1058px;background:var(--white);overflow:hidden}
.page--home{top:60px;height:542px}
.page--solutions{top:639px;height:1992px}

.site-header{position:absolute;left:0;top:0;width:100%;height:62px;background:var(--black)}
.brand{position:absolute;left:127px;top:14px;font-size:27px;font-weight:700;color:var(--white);letter-spacing:.2px}
.main-nav a{position:absolute;top:24px;font-size:11px;color:#cfcfcf;text-decoration:none}
.main-nav a.is-active{color:var(--white);text-decoration:underline}
.call{position:absolute;left:784px;top:13px;display:flex;align-items:center;gap:10px}
.call__icon{width:36px;height:36px;border-radius:50%;background:var(--white);display:flex;align-items:center;justify-content:center}
.call__number{font-size:17px;color:var(--white);font-weight:500}

.hero{position:absolute;left:0;top:62px;width:100%;height:437px}
.hero__photo{position:absolute;inset:0;background:linear-gradient(115deg,#e9b47a 0%,#f1e4d6 28%,#e9eef2 52%,#b9cfe0 72%,#6f7c86 100%)}
.hero__copy{position:absolute;left:127px;top:100px;width:260px;color:var(--ink)}
.hero__title{font-size:22px;font-weight:500;line-height:26px;text-transform:uppercase}
.hero__text{margin-top:6px;font-size:11.2px;line-height:17px}
.lead-panel{position:absolute;left:705px;top:0;width:353px;height:100%;background:var(--panel)}
.lead-panel__title{position:absolute;left:21px;top:102px;font-size:17px;color:var(--white);font-weight:500}
.field{position:absolute;left:23px;width:203px;height:35px;background:var(--white);font-size:10px;color:#333;padding:12px 13px}
.cta{position:absolute;left:23px;top:263px;width:203px;height:35px;background:var(--teal);color:var(--white);font-size:13px;font-weight:500;text-align:center;line-height:35px}
.dots{position:absolute;left:480px;top:409px;display:flex;gap:14px}
.dots span{width:14px;height:14px;border-radius:50%;border:2px solid #222;background:transparent}
.dots span.is-current{background:#111}

.site-footer{position:absolute;left:0;width:100%;height:43px;background:var(--black)}
.page--home .site-footer{top:499px}
.page--solutions .site-footer{top:1949px}
.site-footer__copy{position:absolute;left:127px;top:15px;font-size:10.5px;color:#8d8d8d}
.social{position:absolute;left:816px;top:15px;display:flex;gap:21px}
.social span{width:12px;height:12px;border-radius:50%;background:#8d8d8d}

.page-title{position:absolute;left:0;top:62px;width:100%;height:85px;background:var(--band)}
.page-title h1{position:absolute;left:127px;top:18px;font-size:41px;font-weight:500;color:#a9a9a9}

.media{position:absolute;width:269px;height:269px}
.media__shadow{position:absolute;left:0;top:7px;width:262px;height:262px;background:var(--shadow)}
.media__photo{position:absolute;left:7px;top:0;width:262px;height:262px}
.service{position:absolute}
.service h2{font-size:20.5px;font-weight:500;color:var(--ink);line-height:26px}
.service h2::after{content:"";display:block;width:112px;height:3px;background:var(--teal);margin-top:12px}
.service p{margin-top:16px;font-size:11.2px;line-height:17px}
.ticks{list-style:none;margin-top:10px}
.service h2 + .ticks{margin-top:14px}
.ticks li{position:relative;padding-left:18px;font-size:11.2px;line-height:17px;margin-bottom:17px}
.ticks li::before{content:"";position:absolute;left:0;top:4px;width:9px;height:9px;border-radius:50%;background:var(--teal)}
.ticks li::after{content:"";position:absolute;left:3px;top:5.5px;width:2px;height:4px;border:solid var(--white);border-width:0 1.3px 1.3px 0;transform:rotate(45deg)}
</style>
</head>
<body>

<section class="page page--home">
  <header class="site-header">
    <div class="brand">Brenvora</div>
    <nav class="main-nav">
      <a class="is-active" href="#" style="left:407px">Home</a>
      <a href="#" style="left:459px">Solutions</a>
      <a href="#" style="left:527px">How we do it</a>
      <a href="#" style="left:611px">Our people</a>
      <a href="#" style="left:686px">Our techonology</a>
    </nav>
    <div class="call">
      <span class="call__icon"><svg width="16" height="16" viewBox="0 0 24 24"><path fill="#222" d="M6.6 10.8a15.1 15.1 0 0 0 6.6 6.6l2.2-2.2c.3-.3.7-.4 1-.2 1.1.4 2.3.6 3.6.6.6 0 1 .4 1 1V20c0 .6-.4 1-1 1A17 17 0 0 1 3 4c0-.6.4-1 1-1h3.5c.6 0 1 .4 1 1 0 1.3.2 2.5.6 3.6.1.3 0 .7-.2 1z"/></svg></span>
      <span class="call__number">555 018 2741</span>
    </div>
  </header>

  <div class="hero">
    <div class="hero__photo" role="img" aria-label="Photo of a laptop, tablet, pen and printed charts on a desk"></div>
    <div class="hero__copy">
      <h2 class="hero__title">Delivering global media intelligence</h2>
      <p class="hero__text">Brenvora is an international media intelligence service provider. We help communications teams build and operate truly global media monitoring and measurement programmes.</p>
    </div>
    <form class="lead-panel">
      <div class="lead-panel__title">Learn more about Brenvora</div>
      <div class="field" style="top:136px">Name</div>
      <div class="field" style="top:178px">Phone</div>
      <div class="field" style="top:221px">Email</div>
      <div class="cta">GET STARTED</div>
    </form>
    <div class="dots"><span class="is-current"></span><span></span><span></span><span></span></div>
  </div>

  <footer class="site-footer">
    <div class="site-footer__copy">Copyright &copy; 2019 &nbsp;Brenvora. &nbsp;All rights reserved.</div>
    <div class="social"><span></span><span></span><span></span><span></span></div>
  </footer>
</section>

<section class="page page--solutions">
  <header class="site-header">
    <div class="brand">Brenvora</div>
    <nav class="main-nav">
      <a class="is-active" href="#" style="left:407px">Home</a>
      <a href="#" style="left:459px">Solutions</a>
      <a href="#" style="left:527px">How we do it</a>
      <a href="#" style="left:611px">Our people</a>
      <a href="#" style="left:686px">Our techonology</a>
    </nav>
    <div class="call">
      <span class="call__icon"><svg width="16" height="16" viewBox="0 0 24 24"><path fill="#222" d="M6.6 10.8a15.1 15.1 0 0 0 6.6 6.6l2.2-2.2c.3-.3.7-.4 1-.2 1.1.4 2.3.6 3.6.6.6 0 1 .4 1 1V20c0 .6-.4 1-1 1A17 17 0 0 1 3 4c0-.6.4-1 1-1h3.5c.6 0 1 .4 1 1 0 1.3.2 2.5.6 3.6.1.3 0 .7-.2 1z"/></svg></span>
      <span class="call__number">555 018 2741</span>
    </div>
  </header>

  <div class="page-title"><h1>Solutions</h1></div>

  <!-- Content Sourcing -->
  <div class="media" style="left:127px;top:219px">
    <div class="media__shadow"></div>
    <div class="media__photo" role="img" aria-label="Photo of a hand touching a translucent digital dashboard screen" style="background:linear-gradient(135deg,#4d6572,#a9c2cf 45%,#d8e4ea 65%,#5d707a)"></div>
  </div>
  <article class="service" style="left:418px;top:225px;width:513px">
    <h2>Content Sourcing</h2>
    <p>We help you build a content strategy that meets your budget and coverage needs across earned media - Print, Online, TV and Radio.</p>
    <ul class="ticks">
      <li>Identify geographies and markets of interest</li>
      <li>Build target media source lists to fulfil monitoring and measurement requirements</li>
      <li>Using our transparent cost calculator, we help you with accurate budgeting and choices to ensure you meet your strategy and objectives</li>
      <li>Translate and localise keyword searches and editorial instructions into effecient source-/ country-/ provider-specific needs to minimise wasted content.</li>
    </ul>
  </article>

  <!-- Content Collection -->
  <article class="service" style="left:127px;top:646px;width:495px">
    <h2>Content Collection</h2>
    <p>We consolidate and manage the delivery of your global media content into a Cloud-based scalable media platform, taking the headache of content management away from your teams.</p>
  </article>
  <div class="media" style="left:662px;top:559px">
    <div class="media__shadow"></div>
    <div class="media__photo" role="img" aria-label="Photo of a hand holding a tablet showing a news page over a city and world map" style="background:linear-gradient(135deg,#6f8660,#2f4a30 40%,#1d2c24 70%,#3b5546)"></div>
  </div>

  <!-- Content Augmentation -->
  <div class="media" style="left:127px;top:896px">
    <div class="media__shadow"></div>
    <div class="media__photo" role="img" aria-label="Photo of hands arranging sticky notes on wireframe sketches" style="background:linear-gradient(160deg,#8a7468,#e6d8d8 35%,#f2e6ea 60%,#eee39a 100%)"></div>
  </div>
  <article class="service" style="left:418px;top:873px;width:513px">
    <h2>Content Augmentation</h2>
    <ul class="ticks">
      <li>We manage and normalise all of the source-level reference data - country, language, reach etc.</li>
      <li>We add editorial validation to ensure only the content required reaches your delivery, removing inevitable noise from source providers</li>
      <li>Tagging - AI and human based tagging to detect locations, people, topics, products, brands, services, etc.</li>
      <li>Human and automated grouping of stories across geographies - clustering, "also-in" groupings etc.</li>
      <li>Translation summarisation - AI Translation or human-created depending on budget, speed of delivery and need.</li>
      <li>Digest authoring - refining the essence of today's coverage into a concise board-ready output for your organisation</li>
    </ul>
  </article>

  <!-- Content Delivery -->
  <article class="service" style="left:127px;top:1288px;width:505px">
    <h2>Content Delivery</h2>
    <p>Early morning delivery of a consolidated, ready-to-consume media coverage</p>
    <ul class="ticks">
      <li>Customised email templates, delivering content in templates designed to meet your needs</li>
      <li>Customised platform - modern portal tailored to meet your media management needs, removing the unwanted clutter and focusing on the job at hand</li>
      <li>Integration with Intranets, third-party communication tools e.g. Chatterly, RSS readers, customised APIs</li>
    </ul>
  </article>
  <div class="media" style="left:662px;top:1254px">
    <div class="media__shadow"></div>
    <div class="media__photo" role="img" aria-label="Photo of hands typing on a laptop beside a notepad and pen" style="background:linear-gradient(150deg,#cfd6d4,#f4f3ee 40%,#e7e4dc 70%,#bfc6c9)"></div>
  </div>

  <!-- Media Insights & Consultancy -->
  <div class="media" style="left:127px;top:1604px">
    <div class="media__shadow"></div>
    <div class="media__photo" role="img" aria-label="Photo of an office worker on a phone call taking notes at a desk" style="background:linear-gradient(135deg,#a08a76,#e3d6c8 40%,#f3f1ee 70%,#c9cfd4)"></div>
  </div>
  <article class="service" style="left:418px;top:1590px;width:513px">
    <h2>Media Insights &amp; Consultancy</h2>
    <ul class="ticks">
      <li>Levering the normalised content sets from your integrated monitoring service, we can analyse and tag your coverage based on complex qualitative measurement criteria, consistent across all languages and geographies, to combine with quantitative metrics.</li>
      <li>Ability to create a single consistent measurement programme across all of your global operations.</li>
      <li>Consultancy to HQ and local offices on how to utilise and align existing measurement and insight intiatives to provide continuity.</li>
      <li>Customised online dashboards with near real time data insights, coupled with Board-ready offline reporting and export options.</li>
      <li>Integration with social media content, third-party data, point-of-sale, WebMetrics, and delivering on your Integrated Communications Framework</li>
    </ul>
  </article>

  <footer class="site-footer">
    <div class="site-footer__copy">Copyright &copy; 2019 &nbsp;Brenvora. &nbsp;All rights reserved.</div>
    <div class="social"><span></span><span></span><span></span><span></span></div>
  </footer>
</section>

</body>
</html>
```